Patent Law

Need to develop a home page for a patent lawyer.

Colors should go with logo, blues...

Company Name- Corvel Tindry, PLLC

Company Overview-

I am an Intellectual Property Lawyer and focus on patents, copyrights, trademarks, & trade secrets. I work with small businesses and start ups in the chemical and biotech industries.

Why Us-

I am small firm that can provide large-firm service at a reasonable price. I also can charge flat-fees for entreprenuers in certain practice areas.

Services-
Intellectual Property
Patents
Copyrights
Trademarks
Trade secrets
Healthcare Compliance
Elder law
Wills
Trusts

Website we like-
http://www.quarnlowtide.example/ - within industry!!
http://www.vopperhask.example/
http://dulbrickovan.example/
http://thefernwoldguides.example/

Target Market(s)

My customers will be small business, specifically small start-up companies in the chemical and biotech arena.

Industry/Entity Type

Trade

Requirements
Must have
• Colors should go with logo, blues...

```html
<!DOCTYPE html>
<html lang="en">
<head>
<meta charset="utf-8">
<title>Corvel Tindry, PLLC — Home</title>
<link href="https://fonts.googleapis.com/css2?family=Open+Sans:wght@400;600&family=Cinzel:wght@400&display=swap" rel="stylesheet">
<style>
  :root {
    --teal-light: #a9ecee;
    --teal: #78cfd2;
    --teal-deep: #56b3b7;
    --nav-dark: #2f3436;
    --nav-mid: #45494b;
    --link-blue: #2fb6cf;
    --navy: #2b3f8f;
    --ink: #1f3a3c;
    --box-text: #3f5a5c;
    --white: #ffffff;
    --frame: #8d9497;
  }
  * { margin: 0; padding: 0; box-sizing: border-box; }
  html, body { width: 1200px; height: 906px; overflow: hidden; }
  body {
    position: relative;
    font-family: "Open Sans", Arial, sans-serif;
    background:
      radial-gradient(ellipse 600px 320px at 600px 120px, rgba(220,255,255,0.75), rgba(220,255,255,0) 70%),
      linear-gradient(180deg, var(--teal-light) 0%, var(--teal) 45%, var(--teal-deep) 100%);
  }

  /* Top navigation */
  .site-nav {
    position: absolute; top: 0; left: 0; width: 1200px; height: 35px;
    background: linear-gradient(180deg, var(--nav-mid), var(--nav-dark));
    box-shadow: 0 2px 4px rgba(0,0,0,0.25);
  }
  .nav-links { list-style: none; position: absolute; left: 179px; top: 0; display: flex; height: 35px; }
  .nav-links li {
    color: #f2f2f2; font-size: 12.5px; line-height: 35px; padding: 0 15px;
    border-left: 1px solid rgba(255,255,255,0.12); text-shadow: 0 1px 1px #000;
  }
  .nav-links li:first-child { border-left: none; }
  .nav-links li.is-active {
    background: linear-gradient(180deg, #1aa0b0, #0d7d8c);
    height: 43px; padding: 0 7px; width: 74px; text-align: center;
    clip-path: polygon(0 0,100% 0,100% 86%,50% 100%,0 86%);
  }
  .nav-contact { position: absolute; right: 162px; top: 0; display: flex; align-items: center; height: 35px; color: var(--link-blue); font-size: 14px; }
  .nav-contact svg { margin-right: 4px; }
  .nav-contact .map-link { margin-right: 6px; }

  /* Brand */
  .brand { position: absolute; top: 66px; left: 0; width: 1200px; text-align: center; }
  .brand-mark { width: 52px; height: 52px; border-radius: 50%; background: var(--navy); margin: 0 auto 12px; }
  .brand-name { font-family: "Cinzel", Georgia, serif; font-size: 15px; color: #2a3a4a; letter-spacing: 0.5px; }

  /* Slider */
  .slider { position: absolute; left: 0; top: 180px; width: 1200px; height: 360px; }
  .slider-track { position: absolute; left: 0; top: 0; }
  .slide-photo {
    position: absolute; border-radius: 50%;
    border: 6px solid var(--frame);
    box-shadow: 0 0 0 2px #d9dcdd inset, 0 14px 16px -8px rgba(0,60,70,0.45);
  }
  .slide-photo.main {
    left: 416px; top: -12px; width: 344px; height: 344px;
    background: radial-gradient(circle at 35% 35%, #cdd6dc, #6f7c86 55%, #3a3f46);
  }
  .slide-photo.side-left {
    left: 212px; top: 68px; width: 166px; height: 166px;
    background: radial-gradient(circle at 40% 40%, #e6dcd2, #98a4ae 60%, #4c5561);
  }
  .slide-photo.side-right {
    left: 808px; top: 68px; width: 166px; height: 166px;
    background: radial-gradient(circle at 40% 40%, #cfd9e3, #7d8fa2 60%, #3a4452);
  }

  /* Info boxes */
  .info-box {
    position: absolute; top: 600px; width: 263px; height: 173px;
    border-radius: 10px;
    background: linear-gradient(180deg, rgba(200,250,250,0.7), rgba(150,225,228,0.45));
    box-shadow: 0 3px 8px rgba(0,80,90,0.25), inset 0 0 12px rgba(255,255,255,0.6);
    padding: 9px 14px 0;
  }
  .info-box.why { left: 174px; }
  .info-box.services { left: 469px; }
  .info-box.contact { left: 758px; }
  .info-box h2 {
    font-weight: 400; font-size: 15px; color: var(--ink);
    border-bottom: 1px solid rgba(60,90,95,0.35); padding-bottom: 3px; margin-bottom: 10px;
  }
  .why p { font-family: Arial, sans-serif; font-size: 11.6px; line-height: 15px; color: #1e2a2b; padding-right: 6px; }
  .view-more {
    position: absolute; right: 19px; bottom: 17px;
    background: linear-gradient(180deg, #4a58b8, #26308a); color: var(--white);
    font-family: Arial, sans-serif; font-size: 10.5px; padding: 4px 7px; border-radius: 10px;
  }
  .service-list { list-style: none; font-size: 12.3px; line-height: 15.5px; color: var(--box-text); }
  .contact-list { list-style: none; font-size: 12.3px; color: var(--box-text); }
  .contact-list li { display: flex; align-items: flex-start; margin-bottom: 14px; line-height: 14px; }
  .contact-list svg { flex: none; margin-right: 9px; }

  /* Footer */
  .site-footer { position: absolute; left: 0; top: 790px; width: 1200px; height: 116px; }
  .copyright { position: absolute; left: 179px; top: 75px; font-family: Arial, sans-serif; font-size: 11px; color: #222; }
  .social-links { position: absolute; left: 923px; top: 63px; display: flex; gap: 12px; }
  .social-links span { width: 28px; height: 28px; border-radius: 3px; display: block; }
  .social-links .s1 { background: #2e5fa8; }
  .social-links .s2 { background: #3a9cc8; }
  .social-links .s3 { background: #e0762c; }
</style>
</head>
<body>

<nav class="site-nav">
  <ul class="nav-links">
    <li class="is-active">Homepage</li>
    <li>About Corvel</li>
    <li>Practice Area</li>
    <li>Lawyers</li>
    <li>Case Study</li>
    <li>Contact Us</li>
  </ul>
  <div class="nav-contact">
    <svg width="10" height="14" viewBox="0 0 10 14"><path d="M5 0a5 5 0 0 0-5 5c0 4 5 9 5 9s5-5 5-9a5 5 0 0 0-5-5z" fill="var(--link-blue)"/><circle cx="5" cy="5" r="1.8" fill="var(--nav-dark)"/></svg>
    <span class="map-link">Our Map Location</span>
    <svg width="19" height="19" viewBox="0 0 19 19"><circle cx="9.5" cy="9.5" r="8.5" fill="none" stroke="var(--link-blue)" stroke-width="1.5"/><path d="M6.5 5.5c1-1 1.6-.2 2 .8.3.8-.6 1.2-.3 1.8.5 1.2 1.4 2.1 2.5 2.6.6.3 1-.6 1.8-.3 1 .4 1.8 1 .8 2-1.5 1.6-4 .2-5.6-1.5C6.1 9.3 5 7 6.5 5.5z" fill="var(--link-blue)"/></svg>
    <span>555 019 3400</span>
  </div>
</nav>

<header class="brand">
  <div class="brand-mark"></div>
  <div class="brand-name">CORVEL TINDRY, PLLC</div>
</header>

<section class="slider">
  <svg class="slider-track" width="1200" height="360" viewBox="0 0 1200 360">
    <path d="M164 18 L137 45 L164 73" fill="none" stroke="#2f7f87" stroke-width="1.5"/>
    <path d="M1041 18 L1068 45 L1041 73" fill="none" stroke="#2f7f87" stroke-width="1.5"/>
    <path d="M168 68 Q 190 140 240 150 Q 330 240 430 245" fill="none" stroke="#c9f6f7" stroke-width="2"/>
    <path d="M1035 68 Q 1010 140 960 150 Q 870 240 750 245" fill="none" stroke="#c9f6f7" stroke-width="2"/>
  </svg>
  <div class="slide-photo side-left" role="img" aria-label="Photo of colleagues applauding in a meeting"></div>
  <div class="slide-photo main" role="img" aria-label="Photo of a lawyer in a suit with a team meeting behind him"></div>
  <div class="slide-photo side-right" role="img" aria-label="Photo of two colleagues reviewing work on a laptop"></div>
</section>

<svg style="position:absolute;left:0;top:550px" width="1200" height="40" viewBox="0 0 1200 40">
  <path d="M106 36 Q 600 -12 1121 36" fill="none" stroke="#c6f7f8" stroke-width="2.5"/>
</svg>

<section class="info-box why">
  <h2>WHY US?</h2>
  <p>Lorem ipsum dolor sit amet, consectetuer adipiscing elit, sed diam nonummy nibh euismod tincidunt ut laoreet dolore magna aliquam erat volutpat. Ut wisi enim ad minim veniam, quis nostrud exerci...</p>
  <span class="view-more">View more</span>
</section>

<section class="info-box services">
  <h2>WHAT WE DO?</h2>
  <ul class="service-list">
    <li>Intellectual Property</li>
    <li>Patents</li>
    <li>Copyrights</li>
    <li>Trademarks</li>
    <li>Trade secrets</li>
    <li>Healthcare Compliance</li>
    <li>Elder law</li>
    <li>Wills</li>
  </ul>
</section>

<section class="info-box contact">
  <h2>CONTACT INFORMATION</h2>
  <ul class="contact-list">
    <li>
      <svg width="12" height="17" viewBox="0 0 10 14"><path d="M5 0a5 5 0 0 0-5 5c0 4 5 9 5 9s5-5 5-9a5 5 0 0 0-5-5z" fill="var(--navy)"/><circle cx="5" cy="5" r="1.8" fill="#bfeeee"/></svg>
      <span>Address: Merrow Lane . Suite 48<br>Halvern,NY</span>
    </li>
    <li>
      <svg width="13" height="15" viewBox="0 0 13 15"><path d="M2 1c1.5-1 2.3.3 2.8 1.5.4 1-.8 1.5-.4 2.3.8 1.7 2 3.2 3.6 4 .8.4 1.3-.8 2.3-.4 1.3.6 2.4 1.5 1.2 2.8C9.5 13.5 6 12 3.8 9.5 1.6 7 0 3 2 1z" fill="var(--navy)"/></svg>
      <span>Phone: 5550 193 47</span>
    </li>
    <li>
      <svg width="16" height="15" viewBox="0 0 16 15"><rect x="4" y="0" width="8" height="5" fill="var(--navy)"/><rect x="0" y="5" width="16" height="7" rx="1.5" fill="var(--navy)"/><rect x="4" y="9" width="8" height="6" fill="#d8f4f4" stroke="var(--navy)"/></svg>
      <span>Fax: 55501 934 48</span>
    </li>
  </ul>
</section>

<footer class="site-footer">
  <svg style="position:absolute;left:0;top:0" width="1200" height="116" viewBox="0 0 1200 116">
    <defs>
      <linearGradient id="footer-fill" x1="0" y1="0" x2="0" y2="1">
        <stop offset="0" stop-color="#ececec"/>
        <stop offset="1" stop-color="#ffffff"/>
      </linearGradient>
    </defs>
    <path d="M0 30 Q 600 -18 1200 30 L1200 116 L0 116 Z" fill="url(#footer-fill)"/>
    <path d="M0 30 Q 600 -18 1200 30" fill="none" stroke="#ffffff" stroke-width="3"/>
  </svg>
  <p class="copyright">Copyrights 2014.CORVEL TINDRY,PLLC, All Rights Reserved.</p>
  <div class="social-links">
    <span class="s1"></span><span class="s2"></span><span class="s3"></span>
  </div>
</footer>

</body>
</html>
```